Business Card Design for general contractor or developer

General Contractors. We build new buildings as well as redesign and/or remodel existing buildings. Mostly residential, but we want to expand to commercial as well, so we want the design not to be residential specific.We want the design to be modern, but necessarily minimalistic. A monogram type is also a consideration, but would like to see all ideas.

Target Market(s)

Real estate investors, homeowners, future homeowners, commercial building owners

Industry/Entity Type

Contractor

Contact Information for Business Card

BRIMCOVE Developers Corp, 2917 NE 88th Avenue Suite 412 Coral Springs, FL 33071, Darren Kopec, (305) 555-0148, darren@brimcovedev.example

Font styles to use
Other font styles liked:
• Modern type font

Requirements
Must have
• Must be modern looking
Nice to have
• Metallic type or a standout feature
Should not have
• Tools, floorplans

```html
<!DOCTYPE html>
<html lang="en">
<head>
<meta charset="utf-8">
<title>BRIMCOVE Developers Corp – Business Card</title>
<link rel="stylesheet" href="https://fonts.googleapis.com/css2?family=Oswald:wght@400;500;600&display=swap">
<style>
  :root {
    --stage: #141414;
    --card-dark: #0b0b0b;
    --card-mid: #1c1c1c;
    --card-sheen: #4a4a4a;
    --silver: #c9c9c9;
    --silver-soft: #9a9a9a;
    --rule: #8a8a8a;
  }
  * { margin: 0; padding: 0; box-sizing: border-box; }
  html, body {
    width: 1200px; height: 871px; overflow: hidden;
    background: var(--stage);
    font-family: "Oswald", sans-serif;
    color: var(--silver);
  }
  .canvas {
    position: relative; width: 1200px; height: 871px;
    display: flex; flex-direction: column; align-items: center; justify-content: center; gap: 56px;
  }
  .card {
    position: relative; width: 640px; height: 366px; overflow: hidden;
    border-radius: 4px;
    box-shadow: 0 20px 40px rgba(0,0,0,.6);
  }
  .card-surface {
    position: absolute; inset: 0;
    background: linear-gradient(115deg, var(--card-sheen) 0%, var(--card-mid) 38%, var(--card-dark) 62%, var(--card-dark) 100%);
  }

  /* Front: brand side */
  .front { display: flex; flex-direction: column; align-items: center; justify-content: center; }
  .front .brand-mark { position: relative; width: 96px; height: 96px; border: 4px solid var(--silver); border-radius: 50%; margin-bottom: 26px; }
  .front .brand-name { position: relative; font-size: 46px; font-weight: 500; letter-spacing: 14px; line-height: 1; padding-left: 14px; }
  .front .brand-sub { position: relative; font-size: 20px; font-weight: 400; letter-spacing: 8px; text-transform: uppercase; margin-top: 12px; color: var(--silver); }
  .front .brand-places { position: relative; font-size: 16px; letter-spacing: 1px; margin-top: 10px; color: var(--silver-soft); }

  /* Back: contact side */
  .back { display: flex; align-items: center; }
  .back .brand-block { position: relative; width: 250px; display: flex; flex-direction: column; align-items: center; gap: 14px; }
  .back .brand-mark { width: 120px; height: 120px; border: 5px solid var(--silver); border-radius: 50%; }
  .back .brand-name { font-size: 24px; font-weight: 500; letter-spacing: 6px; }
  .back .divider { position: relative; width: 2px; height: 230px; background: var(--rule); }
  .contact { position: relative; padding-left: 30px; }
  .contact-name { font-size: 36px; font-weight: 600; letter-spacing: 2px; margin-bottom: 10px; }
  .contact-row { display: flex; align-items: flex-start; gap: 12px; font-size: 19px; font-weight: 500; letter-spacing: 1.5px; line-height: 1.4; margin-top: 4px; }
  .contact-row svg { flex: none; margin-top: 5px; fill: var(--silver); }
</style>
</head>
<body>
<main class="canvas">

  <section class="card front" aria-label="Business card front">
    <div class="card-surface" role="img" aria-label="Glossy black card stock with faint square grid texture"></div>
    <div class="brand-mark"></div>
    <div class="brand-name">BRIMCOVE</div>
    <div class="brand-sub">Developers Corp</div>
    <div class="brand-places">Miami | Houston | Dallas, TX</div>
  </section>

  <section class="card back" aria-label="Business card back">
    <div class="card-surface" role="img" aria-label="Glossy black card stock with faint square grid texture"></div>
    <div class="brand-block">
      <div class="brand-mark"></div>
      <div class="brand-name">BRIMCOVE</div>
    </div>
    <div class="divider"></div>
    <div class="contact">
      <div class="contact-name">Darren Kopec</div>
      <div class="contact-row">
        <svg width="14" height="18" viewBox="0 0 14 18" aria-hidden="true"><path d="M7 0a7 7 0 0 0-7 7c0 5 7 11 7 11s7-6 7-11a7 7 0 0 0-7-7zm0 10a3 3 0 1 1 0-6 3 3 0 0 1 0 6z"/></svg>
        <span>2917 NE 88th Avenue<br>Suite 412 Coral Springs FL 33071</span>
      </div>
      <div class="contact-row">
        <svg width="16" height="16" viewBox="0 0 16 16" aria-hidden="true"><path d="M3.5 1l2.5 3-1.5 2c1 2 3 4 5 5l2-1.5 3 2.5-1.5 2.5C8 15 1 8 1 2.5z"/></svg>
        <span>(305) 555-0148</span>
      </div>
      <div class="contact-row">
        <svg width="16" height="12" viewBox="0 0 16 12" aria-hidden="true"><path d="M0 0h16v12H0zM1.5 1.5v.4L8 6.5l6.5-4.6v-.4zM1.5 3.7v6.8h13V3.7L8 8.3z"/></svg>
        <span>darren@brimcovedev.example</span>
      </div>
    </div>
  </section>

</main>
</body>
</html>
```